Cedar Lantern Letterhead

I just need letterhead for my integrative psychiatry business. I'm going to use this to do mailings to other doctors, as well as send letters to patients. Thank you

Business

```html
<!DOCTYPE html>
<html lang="en">
<head>
<meta charset="utf-8">
<title>Cedar Lantern Letterhead</title>
<link rel="stylesheet" href="https://fonts.googleapis.com/css2?family=Source+Sans+3:wght@400;600&display=swap">
<style>
  :root {
    --backdrop: #d4d5d7;
    --paper: #ecedef;
    --leaf-green: #2e7a3a;
    --bark-brown: #6b2f16;
  }
  * { margin: 0; padding: 0; box-sizing: border-box; }
  html, body {
    width: 1200px;
    height: 848px;
    overflow: hidden;
    background: var(--backdrop);
    font-family: "Source Sans 3", "Myriad Pro", Arial, sans-serif;
  }
  .letterhead {
    position: absolute;
    left: 350px;
    top: 72px;
    width: 498px;
    height: 704px;
    background: var(--paper);
  }
  .header-rules {
    position: absolute;
    left: 0;
    top: 0;
    width: 498px;
    height: 60px;
  }
  .brand {
    position: absolute;
    left: 136px;
    top: 68px;
    display: flex;
    align-items: center;
    gap: 6px;
    color: var(--leaf-green);
    font-size: 15px;
    font-weight: 600;
    letter-spacing: 0.2px;
  }
  .brand-dot {
    width: 9px;
    height: 9px;
    border-radius: 50%;
    background: var(--bark-brown);
  }
  .contact {
    position: absolute;
    left: 24px;
    top: 634px;
    font-size: 8px;
    line-height: 7.6px;
    color: var(--leaf-green);
    font-style: normal;
  }
  .credentials {
    position: absolute;
    right: 15px;
    top: 656px;
    text-align: right;
    font-size: 8px;
    line-height: 7px;
    color: var(--leaf-green);
  }
  .credentials .physician {
    color: var(--bark-brown);
    margin-bottom: 4px;
    line-height: 8px;
  }
</style>
</head>
<body>
  <main class="letterhead">
    <svg class="header-rules" viewBox="0 0 498 60" aria-hidden="true">
      <rect x="24" y="30" width="250" height="2.5" fill="var(--leaf-green)"/>
      <rect x="224" y="38" width="250" height="2.5" fill="var(--bark-brown)"/>
    </svg>

    <div class="brand">
      <span class="brand-dot"></span>
      <span class="brand-name">Cedar Lantern</span>
    </div>

    <address class="contact">
      916-555-0142<br>
      916-555-0143<br>
      2870 Alder Creek Road<br>
      Suite 210<br>
      Pine Hollow, CA 95612<br>
      www.cedarlanternwellness.com
    </address>

    <div class="credentials">
      <p class="physician">Elena Varkaris, MD</p>
      <p>Certified, Northwest Council for Clinical Psychiatry</p>
      <p>Certified, Pacific Council for Integrative and Whole-Person Care</p>
    </div>
  </main>
</body>
</html>
```